Make a great menu for our Seafood Restaurant LumVo

Design a iconic menu for my fish restaurant on the island of Phu Quoc, Vietnam. Coastal, seafood and pictures of all menu items inside. For our restaurant menu help us transform our food photos and some saucy sentences into a complete, professional restaurant menu.

A logo is in the works, leave empty space, colors will be mostly blue on lots of white, not all dishes have to be in the menu but most should be in there.

Should be a classy menu, not to busy looking.

Ive attached two samples. Attached also all images.

Target Market(s)

Mostly Asian guests

Industry/Entity Type

Seafood Restaurant

Font styles to use
Sans Serif
Decorative
Script

Colors
3176b5
33a6d7
0692cd
0255a3
85abd2
85cae6
ecf7fb
cfdeed
ffffff

Requirements
Must have
• Sazz, lots of pictures, cool menu, playfull and cheeky, but still classy if this makes any sense.
• Size of menu probably half A3, like 25CM wide by 36 CM high

```html
<!DOCTYPE html>
<html lang="en">
<head>
<meta charset="utf-8">
<title>LumVo Seafood Menu – Four Page Spread</title>
<link href="https://fonts.googleapis.com/css2?family=Roboto:wght@400;500;700&family=Roboto+Condensed:wght@400;500&family=Dancing+Script:wght@600&display=swap" rel="stylesheet">
<style>
:root{
  --blue-deep:#0255a3;
  --blue:#3176b5;
  --blue-bright:#0692cd;
  --sky:#33a6d7;
  --pale:#85abd2;
  --ice:#ecf7fb;
  --mist:#cfdeed;
  --white:#ffffff;
  --sage:#86a99a;
  --sage-dark:#5f927f;
  --ink:#2a3440;
  --line:#b9c9dc;
}
*{box-sizing:border-box;margin:0;padding:0}
html,body{width:918px;height:1200px;overflow:hidden;background:var(--white)}
body{position:relative;font-family:'Roboto',sans-serif;color:var(--ink)}

.page{position:absolute;width:392px;height:554px;overflow:hidden;
  background:linear-gradient(180deg,#f7f9fc 0%,#eef3f8 55%,#f5f7fa 100%);
  box-shadow:0 1px 4px rgba(0,0,0,.25)}
.page-label{position:absolute;width:392px;text-align:center;font-weight:700;font-size:15px;color:#111}

.header-wave{position:absolute;left:0;top:0;width:392px;height:110px}
.brand{position:absolute;left:0;width:100%;text-align:center;font-family:'Roboto',sans-serif;
  font-weight:500;color:var(--sage);letter-spacing:2px}
.footer-rule{position:absolute;left:0;top:526px;width:100%;border-top:1px dashed var(--blue)}
.footer-band{position:absolute;left:0;top:530px;width:100%;height:24px;
  background:linear-gradient(180deg,var(--blue) 0%,var(--blue-deep) 100%);
  color:var(--white);font-size:10px;letter-spacing:2.4px;text-align:center;line-height:22px}

.ph{position:absolute;display:block}
.abs{position:absolute}

.section-title{position:absolute;font-family:'Dancing Script',cursive;font-weight:600;
  color:var(--blue);font-size:9px;white-space:nowrap}
.section-title::before{content:"";display:inline-block;width:5px;height:5px;border-radius:50%;
  background:var(--blue-bright);margin-right:3px;vertical-align:middle}
.frame{position:absolute;border:1px solid var(--mist);background:rgba(255,255,255,.55)}

/* dish card */
.card{position:absolute;width:66px;text-align:center}
.card .photo{position:relative;height:42px;border-radius:2px}
.badge{position:absolute;left:50%;bottom:-5px;transform:translateX(-50%);background:var(--white);
  color:var(--blue-bright);font-weight:700;font-size:6px;padding:1px 6px;border-radius:6px;white-space:nowrap}
.card .name{margin-top:8px;font-size:3.8px;font-weight:700;line-height:1.2;min-height:9px}
.card .desc{margin-top:2px;border:.6px solid var(--line);font-size:3.2px;line-height:1.3;padding:2px;min-height:10px}

/* menu row */
.row{position:absolute;height:18px}
.row .thumb{position:absolute;left:0;top:0;width:22px;height:16px;border-radius:1px}
.row .name{position:absolute;left:26px;top:2px;font-size:4.2px;font-weight:700;white-space:nowrap}
.row .desc{position:absolute;left:26px;top:8px;font-size:3.2px;line-height:1.3;width:90px;color:#444}
.row .price{position:absolute;right:0;top:2px;font-size:4.2px;font-weight:500}
.row .price .veg{color:#4b9a3c}

.circle-dish{position:absolute;width:52px;height:52px;border-radius:50%;border:4px solid var(--white);
  box-shadow:0 1px 3px rgba(0,0,0,.25)}

.intro-box{position:absolute;left:13px;top:356px;width:212px;height:132px;border:1px solid var(--blue);
  background:var(--white);padding:5px 6px;font-size:7px;line-height:1.5;color:var(--blue-deep);text-align:justify}
.intro-box p{margin-bottom:4px}
.headline{position:absolute;left:91px;top:318px;color:var(--blue-deep);font-size:17px;line-height:1.1}
.legend{position:absolute;left:0;top:90px;width:100%;text-align:center;font-size:11px;color:var(--blue)}
.legend .sep{color:#777;margin:0 12px}
.ribbon{position:absolute;left:64px;top:502px;width:264px;height:20px}
.ribbon-text{position:absolute;left:64px;top:505px;width:264px;text-align:center;color:var(--white);
  font-family:'Roboto Condensed',sans-serif;font-size:11px;letter-spacing:.3px}

.list-line{position:absolute;font-size:4.2px;font-weight:700;white-space:nowrap}
.list-sub{position:absolute;font-size:3.2px;color:#444;line-height:1.3}
</style>
</head>
<body>

<!-- ============ PAGE 1 : COVER ============ -->
<section class="page" style="left:31px;top:15px">
  <svg class="header-wave" viewBox="0 0 392 110" aria-hidden="true">
    <path d="M0 0H392V18C300 30 170 40 0 104Z" fill="#0255a3"/>
    <path d="M0 0H392V10C290 20 160 32 0 92Z" fill="#3176b5"/>
    <path d="M0 0H392V4C280 10 150 22 0 80Z" fill="#33a6d7" opacity=".5"/>
  </svg>
  <div class="brand" style="top:22px;font-size:48px">LumVo</div>
  <div class="legend">V Vegetarian<span class="sep">|</span>GF Gluten Free<span class="sep">|</span>☐ Mild Spicy</div>

  <div class="ph" role="img" aria-label="Seafood salad with prawns and greens on a plate" style="left:0;top:114px;width:258px;height:180px;background:linear-gradient(135deg,#5f6d3f 0%,#c9a58a 40%,#e7d2c0 60%,#6b7a43 100%)"></div>
  <div class="ph" role="img" aria-label="Tropical orange cocktail with fruit garnish" style="left:258px;top:114px;width:134px;height:180px;background:linear-gradient(160deg,#e8e2d6 0%,#f4b23a 45%,#e58a1c 75%,#d9cdbd 100%)"></div>

  <div class="ph" role="img" aria-label="Leaping dolphins illustration" style="left:13px;top:310px;width:72px;height:40px;border-radius:40% 60% 30% 70%;background:linear-gradient(135deg,#85abd2,#0255a3)"></div>
  <div class="headline">When it comes to<br>&nbsp;&nbsp;menu ideas....</div>
  <div class="brand" style="left:170px;width:220px;top:322px;font-size:30px">LumVo</div>

  <div class="intro-box">
    <p>At our seafood restaurant we will serve you an eclectic mix of Phu Quoc flavours all visible in the menu with gorgeous pictures and Fusion dishes highlighted as healthy specials.</p>
    <p>Instead of the traditional menu starter/main/dessert you will see our menu setup in a more family style friendly way as people like to eat in Phu Quoc.</p>
    <p>From our menu you will be able to choose from our wok, grill, raw, smoke, steam, fried and be able to combine these dishes into a big family style platter.</p>
  </div>
  <div class="ph" role="img" aria-label="Charcuterie platter with sliced meats and pickles" style="left:226px;top:356px;width:166px;height:132px;border-radius:60% 0 0 50%;background:radial-gradient(circle at 60% 55%,#c96a6a 0%,#e4b0a8 40%,#f1ece6 70%,#eef2f6 100%)"></div>

  <svg class="ribbon" viewBox="0 0 264 20" aria-hidden="true">
    <polygon points="0,4 14,4 14,18 0,18 6,11" fill="#5f927f"/>
    <polygon points="264,4 250,4 250,18 264,18 258,11" fill="#5f927f"/>
    <rect x="10" y="0" width="244" height="17" fill="#86a99a"/>
  </svg>
  <div class="ribbon-text">QUALITY HERE&nbsp;&nbsp;•&nbsp;&nbsp;MEANS QUALITY HERE</div>

  <div class="footer-rule"></div>
  <div class="footer-band">www.lumvo.com</div>
</section>
<div class="page-label" style="left:31px;top:578px">Page1</div>

<!-- ============ PAGE 2 : HEALTHY / BREAD / MARKET / SOUP / STARTER ============ -->
<section class="page" style="left:494px;top:15px">
  <svg class="header-wave" viewBox="0 0 392 110" aria-hidden="true">
    <path d="M0 0H392V14C300 22 170 30 0 92Z" fill="#0255a3"/>
    <path d="M0 0H392V6C290 14 160 22 0 80Z" fill="#3176b5"/>
  </svg>
  <div class="brand" style="top:20px;font-size:36px">LumVo</div>

  <div class="section-title" style="left:146px;top:84px">Linh's Healthy Choices</div>
  <div class="frame" style="left:16px;top:96px;width:362px;height:80px"></div>
  <div class="card" style="left:22px;top:100px"><div class="photo ph" role="img" aria-label="Herring salad with herbs" style="position:relative;background:linear-gradient(135deg,#e7e2d8,#b7c59a,#d8a48a)"><span class="badge">100 GF</span></div><div class="name">GOI CA TRICH</div><div class="desc">Phu Quoc herring with salad, herbs and rice paper, single or sharing</div></div>
  <div class="card" style="left:94px;top:100px"><div class="photo ph" role="img" aria-label="Fresh spring rolls" style="position:relative;background:linear-gradient(135deg,#e9ddc8,#c8935e,#a7b77a)"><span class="badge">100 GF</span></div><div class="name">A DELICIOUS MIX OF OUR FRESH SPRING ROLLS</div><div class="desc">Fish cake, shrimps, roasted duck, Phu Quoc crab</div></div>
  <div class="card" style="left:166px;top:100px"><div class="photo ph" role="img" aria-label="Oysters on ice" style="position:relative;background:linear-gradient(135deg,#eef0f2,#b6b9b4,#e4e6e8)"><span class="badge">100 GF</span></div><div class="name">VIETNAMESE OYSTERS</div><div class="desc">½ dozen, served on ice with black pepper and lime</div></div>
  <div class="card" style="left:238px;top:100px"><div class="photo ph" role="img" aria-label="Ceviche in avocado halves" style="position:relative;background:linear-gradient(135deg,#dfe6cf,#8fb04c,#e9d9a4)"><span class="badge">100 GF</span></div><div class="name">CEVICHE SWIMMING IN AVOCADO</div><div class="desc">Raw marinated fish, lime, red onion, chili, avocado creme</div></div>
  <div class="card" style="left:310px;top:100px"><div class="photo ph" role="img" aria-label="Poached red snapper" style="position:relative;background:linear-gradient(135deg,#efe5d5,#e2a46a,#d9d2c3)"><span class="badge">100 GF</span></div><div class="name">POACHED RED SNAPPER</div><div class="desc">Spinach bulgur with sous-vide prawn, saffron foam</div></div>

  <div class="section-title" style="left:138px;top:192px">Selection of Our House Bread</div>
  <div class="list-line" style="left:110px;top:208px">SARDINE BUTTER, OLIVE/SHRIMP TAPENADE, VIETNAMESE PATE<span style="margin-left:16px">100</span></div>

  <div class="section-title" style="left:70px;top:230px">Phu Quoc Fish market, See Our Special Daily Fresh Menu Boards</div>
  <div class="frame" style="left:58px;top:242px;width:270px;height:46px"></div>
  <div class="list-line" style="left:64px;top:249px">LOCAL FISH, SQUID, PRAWNS, CLAMS, SHELLS, SNAILS, LOBSTER, CRAB<span style="margin-left:8px">100GF</span></div>
  <div class="list-line" style="left:64px;top:254px">DAY FRESH CATCH</div>
  <div class="list-line" style="left:64px;top:266px">LINH'S PHU QUOC SEAFOOD SHARING PLATE<span style="margin-left:58px">100GF</span></div>
  <div class="list-sub" style="left:64px;top:272px;width:140px">Crab, lobster, oysters, clams, snails, local fish sashimi, prawns, house mayonnaise</div>
  <div class="ph" role="img" aria-label="Seafood sharing bowl" style="left:266px;top:248px;width:54px;height:34px;border-radius:50%;background:radial-gradient(circle,#d8643c,#a7b5a2 60%,#6f7377)"></div>

  <div class="section-title" style="left:22px;top:304px">Chefs specialty, House Smoked Phu Quoc Fish</div>
  <div class="frame" style="left:14px;top:316px;width:212px;height:68px"></div>
  <div class="row" style="left:20px;top:321px;width:138px"><span class="thumb ph" role="img" aria-label="Smoked eel" style="background:linear-gradient(135deg,#e8dccb,#b99070)"></span><span class="name">EEL</span><span class="price">100GF</span></div>
  <div class="row" style="left:20px;top:341px;width:138px"><span class="thumb ph" role="img" aria-label="Smoked barracuda" style="background:linear-gradient(135deg,#ece2d4,#c19a73)"></span><span class="name">BARRACUDA</span><span class="price">100GF</span></div>
  <div class="row" style="left:20px;top:361px;width:138px"><span class="thumb ph" role="img" aria-label="Smoked mackerel" style="background:linear-gradient(135deg,#e6dccd,#aa8768)"></span><span class="name">MACKEREL</span><span class="price">100GF</span></div>
  <div class="ph" role="img" aria-label="Whole smoked fish" style="left:164px;top:346px;width:56px;height:8px;border-radius:4px;transform:rotate(-8deg);background:linear-gradient(90deg,#7a4a25,#b3773f,#6b3e1e)"></div>

  <div class="section-title" style="left:250px;top:296px">Soup</div>
  <div class="frame" style="left:238px;top:308px;width:140px;height:84px"></div>
  <div class="row" style="left:242px;top:313px;width:130px"><span class="thumb ph" role="img" aria-label="Fish soup" style="background:linear-gradient(135deg,#f3e3b0,#d9a84c)"></span><span class="name">LINH'S PHU QUOC CATCH</span><span class="price">100</span><span class="desc" style="width:80px">Local fish soup with shrimps, clams, star anise, croutons</span></div>
  <div class="row" style="left:242px;top:339px;width:130px"><span class="thumb ph" role="img" aria-label="Mushroom soup" style="background:linear-gradient(135deg,#e4e0d6,#a99c86)"></span><span class="name">PHU QUOC TRAM MUSHROOM</span><span class="price">100GF <span class="veg">V</span></span><span class="desc" style="width:80px">Bisque with noodles and spring onion</span></div>
  <div class="row" style="left:242px;top:365px;width:130px"><span class="thumb ph" role="img" aria-label="Tomato soup" style="background:linear-gradient(135deg,#e3823a,#c9482a)"></span><span class="name">HEALTHY DALAT TOMATO</span><span class="price">100GF <span class="veg">V</span></span><span class="desc" style="width:80px">Tomato soup with basil pesto, egg</span></div>

  <div class="section-title" style="left:176px;top:410px">Starter</div>
  <div class="frame" style="left:14px;top:422px;width:364px;height:88px"></div>
  <div class="card" style="left:20px;top:427px"><div class="photo ph" role="img" aria-label="Grilled octopus skewers" style="position:relative;background:linear-gradient(135deg,#e6ddd0,#6b4a36,#b7a58f)"><span class="badge">100</span></div><div class="name">GRILLED OCTOPUS SKEWERS</div><div class="desc">Jacket potato, Phu Quoc black pepper vinaigrette</div></div>
  <div class="card" style="left:92px;top:427px"><div class="photo ph" role="img" aria-label="Roasted caramelized prawns" style="position:relative;background:linear-gradient(135deg,#ece2d2,#d99a62,#b8c08a)"><span class="badge">100</span></div><div class="name">ROASTED AND CARAMELIZED PRAWNS</div><div class="desc">Roasted corn creme, eggplant, fish sauce, honey dressing</div></div>
  <div class="card" style="left:164px;top:427px"><div class="photo ph" role="img" aria-label="Fish charcuterie" style="position:relative;background:linear-gradient(135deg,#f1eee8,#d9b8a0,#e5e7ea)"><span class="badge">100</span></div><div class="name">CHEF'S CHARCUTERSEA</div><div class="desc">Smoked tuna, marinated red snapper, crab cocktail, mango chutney</div></div>
  <div class="card" style="left:236px;top:427px"><div class="photo ph" role="img" aria-label="Crab meat in glass" style="position:relative;background:linear-gradient(135deg,#eef2e6,#c6d68a,#e8e2cf)"><span class="badge">100</span></div><div class="name">PHU QUOC CRAB MEAT</div><div class="desc">Pomelo, sweet potato, avocado creme, crab cracker</div></div>
  <div class="card" style="left:308px;top:427px"><div class="photo ph" role="img" aria-label="Oysters three ways" style="position:relative;background:linear-gradient(135deg,#d9d2cc,#8a6e80,#c9bfb2)"><span class="badge">100 GF</span></div><div class="name">CHEF'S FAVOURITE OYSTERS</div><div class="desc">Three oyster styles: passion fruit, cucumber, coffee, purple yam</div></div>

  <div class="footer-rule"></div>
  <div class="footer-band">www.lumvo.com</div>
</section>
<div class="page-label" style="left:494px;top:578px">Page2</div>

<!-- ============ PAGE 3 : MAIN / VEGETARIAN / SPIRIT / MEAT ============ -->
<section class="page" style="left:32px;top:609px">
  <svg class="header-wave" viewBox="0 0 392 110" aria-hidden="true">
    <path d="M0 0H392V14C300 22 170 30 0 92Z" fill="#0255a3"/>
    <path d="M0 0H392V6C290 14 160 22 0 80Z" fill="#3176b5"/>
  </svg>
  <div class="brand" style="top:20px;font-size:36px">LumVo</div>

  <div class="section-title" style="left:26px;top:84px">Main</div>
  <div class="frame" style="left:14px;top:94px;width:160px;height:148px"></div>
  <div class="row" style="left:18px;top:98px;width:150px"><span class="thumb ph" role="img" aria-label="Grilled tuna" style="background:linear-gradient(135deg,#e8d8c4,#a9653f)"></span><span class="name">GRILLED ROSE TUNA</span><span class="price">100GF</span><span class="desc">Grilled, scallop, beetroot, grapefruit, cress</span></div>
  <div class="row" style="left:18px;top:121px;width:150px"><span class="thumb ph" role="img" aria-label="Squid in coconut" style="background:linear-gradient(135deg,#e2ecd6,#9dbf6a)"></span><span class="name">POACHED SQUID BATHING IN A COCONUT</span><span class="price">100GF</span><span class="desc">Warm poached squid salad, lime, chili, iceberg</span></div>
  <div class="row" style="left:18px;top:144px;width:150px"><span class="thumb ph" role="img" aria-label="Steamed sea bass" style="background:linear-gradient(135deg,#ecebe4,#b9a98a)"></span><span class="name">STEAMED SEA BASS</span><span class="price">100</span><span class="desc">with lemon grass, chilly and lime</span></div>
  <div class="row" style="left:18px;top:167px;width:150px"><span class="thumb ph" role="img" aria-label="Grilled prawns" style="background:linear-gradient(135deg,#eadccb,#d7834b)"></span><span class="name">GRILLED PRAWNS</span><span class="price">100</span><span class="desc">with fresh coconut risotto, cilantro</span></div>
  <div class="row" style="left:18px;top:190px;width:150px"><span class="thumb ph" role="img" aria-label="Baked oysters" style="background:linear-gradient(135deg,#ece6da,#c9a46c)"></span><span class="name">CHEF'S SIGNATURE OYSTERS</span><span class="price">100</span><span class="desc">French savory crepes, oyster, spinach, beurre blanc</span></div>
  <div class="row" style="left:18px;top:213px;width:150px"><span class="thumb ph" role="img" aria-label="Rock lobster" style="background:linear-gradient(135deg,#efe0d0,#cf5a3a)"></span><span class="name">LINH'S ROCK LOBSTER</span><span class="price">100GF</span><span class="desc">Sweet apple, sour yoghurt, bitter melon, salted lemon, mint</span></div>

  <div class="section-title" style="left:230px;top:84px">Vegetarian</div>
  <div class="frame" style="left:218px;top:94px;width:162px;height:148px"></div>
  <div class="row" style="left:222px;top:98px;width:152px"><span class="thumb ph" role="img" aria-label="Vietnamese pancake" style="background:linear-gradient(135deg,#f1d98a,#9bb35a)"></span><span class="name">BANH XEO</span><span class="price">100GF<span class="veg">V</span></span><span class="desc">Vietnamese pancake with tofu, mushroom, bean sprouts, herbs</span></div>
  <div class="row" style="left:222px;top:126px;width:152px"><span class="thumb ph" role="img" aria-label="Vegetable lasagne" style="background:linear-gradient(135deg,#efe3c8,#c98d4f)"></span><span class="name">LINH'S VEGETABLE LASAGNE</span><span class="price">100<span class="veg">V</span></span><span class="desc">Grilled zucchini and eggplant, tomato, ice-cream, sweet potato</span></div>
  <div class="row" style="left:222px;top:154px;width:152px"><span class="thumb ph" role="img" aria-label="Mushroom risotto" style="background:linear-gradient(135deg,#f0ebe0,#b8a27e)"></span><span class="name">RISOTTO AIFUNGHI</span><span class="price">100GF<span class="veg">V</span></span><span class="desc">Italian risotto with local mushroom and parmesan cheese</span></div>
  <div class="row" style="left:222px;top:182px;width:152px"><span class="thumb ph" role="img" aria-label="Green garden salad" style="background:linear-gradient(135deg,#e8efd8,#7faa4a)"></span><span class="name">GREEN GARDEN SALAD</span><span class="price">100<span class="veg">V</span></span><span class="desc">Fresh crispy salad, green mango, papaya and peanuts</span></div>
  <div class="row" style="left:222px;top:210px;width:152px"><span class="thumb ph" role="img" aria-label="Cheese and pepper bites" style="background:linear-gradient(135deg,#ece0c6,#c6903e)"></span><span class="name">SAVOUR CHEESE AND GREEN PEPPER CRISPY "BITTERBALLS"</span><span class="price">100<span class="veg">V</span></span><span class="desc" style="top:13px">Mustard sauce and roasted baby tomato</span></div>

  <div class="section-title" style="left:36px;top:252px">The Spirit of Vietnam</div>
  <div class="frame" style="left:14px;top:264px;width:364px;height:106px"></div>
  <div class="list-line" style="left:174px;top:268px">LOCAL FISH MARKET<span style="margin-left:8px">100GF</span></div>
  <div class="list-sub" style="left:176px;top:274px">See our special daily fresh menu boards</div>
  <div class="card" style="left:20px;top:288px;width:64px"><div class="photo ph" role="img" aria-label="Mackerel and prawn" style="position:relative;height:30px;background:linear-gradient(135deg,#eee7da,#a58763)"><span class="badge">100GF</span></div><div class="name">MACKEREL &amp; PRAWN</div><div class="desc">Grilled with PQ red pepper oil</div></div>
  <div class="card" style="left:116px;top:288px;width:64px"><div class="photo ph" role="img" aria-label="Seafood hotpot" style="position:relative;height:30px;background:linear-gradient(135deg,#e9dfd2,#d06a3c,#7fa55a)"><span class="badge">100GF</span></div><div class="name">HOTPOT</div><div class="desc">Seafood, stock, vegetables, rice noodles, tofu, fish balls</div></div>
  <div class="card" style="left:212px;top:288px;width:64px"><div class="photo ph" role="img" aria-label="Phu Quoc crab" style="position:relative;height:30px;background:linear-gradient(135deg,#c9553a,#8b3a2a,#d9a07a)"><span class="badge">100</span></div><div class="name">PHU QUOC CRAB</div><div class="desc">Stir-fried with egg, green pepper corn</div></div>
  <div class="card" style="left:308px;top:288px;width:64px"><div class="photo ph" role="img" aria-label="Seafood pancake" style="position:relative;height:30px;background:linear-gradient(135deg,#f2e3a8,#7fae4c)"><span class="badge">100 GF</span></div><div class="name">SEAFOOD BANH XEO</div><div class="desc">Vietnamese pancake, seafood, bean sprouts, lettuce</div></div>

  <div class="section-title" style="left:36px;top:380px">Nice to Meat</div>
  <div class="frame" style="left:14px;top:392px;width:364px;height:62px"></div>
  <div class="row" style="left:18px;top:397px;width:150px"><span class="thumb ph" role="img" aria-label="Steak tartare" style="background:linear-gradient(135deg,#e9d6c8,#a8443a)"></span><span class="name">STEAK TARTAR</span><span class="price">100GF</span><span class="desc">Minced beef, egg yolk creme, capers, pickles, PQ white pepper</span></div>
  <div class="row" style="left:18px;top:422px;width:150px"><span class="thumb ph" role="img" aria-label="Charcuterie plate" style="background:linear-gradient(135deg,#efdcd6,#c05e62)"></span><span class="name">CHARCUTERIE</span><span class="price">100</span><span class="desc">Parma ham, sausage, chorizo, pate, salami, pickles, onion</span></div>
  <div class="row" style="left:222px;top:397px;width:150px"><span class="thumb ph" role="img" aria-label="Skirt steak" style="background:linear-gradient(135deg,#d9b49a,#6e3828)"></span><span class="name">SKIRT STEAK</span><span class="price">100GF</span><span class="desc">Grilled, rosemary potato, red wine shallot butter</span></div>
  <div class="row" style="left:222px;top:422px;width:150px"><span class="thumb ph" role="img" aria-label="Veal fillet" style="background:linear-gradient(135deg,#d8b8a6,#7a3e30)"></span><span class="name">VEAL FILLET-TENDERLOIN</span><span class="price">100GF</span><span class="desc">Marinated with PQ black pepper, pumpkin and green beans</span></div>

  <div class="circle-dish ph" role="img" aria-label="Chili crab soup" style="left:12px;top:472px;background:radial-gradient(circle,#d2492a,#a52c1a 60%,#efe6dc 62%)"></div>
  <div class="circle-dish ph" role="img" aria-label="Egg noodles" style="left:89px;top:472px;background:radial-gradient(circle,#f1b236,#d98e1c 60%,#f1ebdf 62%)"></div>
  <div class="circle-dish ph" role="img" aria-label="Fried egg and greens" style="left:169px;top:472px;background:radial-gradient(circle,#f3a21a 0 18%,#ffffff 20% 45%,#7aa94e 55%,#eef0ec 62%)"></div>
  <div class="circle-dish ph" role="img" aria-label="Curry sauce bowl" style="left:249px;top:472px;background:radial-gradient(circle,#c9a01e,#a27f12 60%,#eee9dc 62%)"></div>
  <div class="circle-dish ph" role="img" aria-label="Grilled skewers" style="left:329px;top:472px;background:radial-gradient(circle,#a6572c,#7a3a1c 55%,#eee5dc 62%)"></div>

  <div class="footer-rule"></div>
  <div class="footer-band">www.lumvo.com</div>
</section>
<div class="page-label" style="left:32px;top:1170px">Page3</div>

<!-- ============ PAGE 4 : SIDE / DESSERT ============ -->
<section class="page" style="left:494px;top:609px">
  <svg class="header-wave" viewBox="0 0 392 110" aria-hidden="true">
    <path d="M0 0H392V14C300 22 170 30 0 92Z" fill="#0255a3"/>
    <path d="M0 0H392V6C290 14 160 22 0 80Z" fill="#3176b5"/>
  </svg>
  <div class="brand" style="top:20px;font-size:36px">LumVo</div>

  <div class="section-title" style="left:30px;top:84px">Side</div>
  <div class="row" style="left:20px;top:104px;width:150px"><span class="thumb ph" role="img" aria-label="Tram mushrooms" style="background:linear-gradient(135deg,#e6d9c6,#9c7a56)"></span><span class="name">PHU QUOC'S FAMOUS TRAM MUSHROOM</span><span class="price">100GF<span class="veg">V</span></span><span class="desc">Sauteed</span></div>
  <div class="row" style="left:20px;top:132px;width:150px"><span class="thumb ph" role="img" aria-label="Morning glory" style="background:linear-gradient(135deg,#d6e6c2,#4f8a32)"></span><span class="name">MORNING GLORY</span><span class="price">100GF<span class="veg">V</span></span><span class="desc">Stir fried with garlic</span></div>
  <div class="row" style="left:20px;top:160px;width:150px"><span class="thumb ph" role="img" aria-label="Thienly flowers" style="background:linear-gradient(135deg,#dbe8c8,#5c9440)"></span><span class="name">THIENLY FLOWERS</span><span class="price">100GF<span class="veg">V</span></span><span class="desc">Sauteed</span></div>
  <div class="row" style="left:20px;top:190px;width:150px"><span class="thumb ph" role="img" aria-label="Grilled eggplant" style="background:linear-gradient(135deg,#7a6a4a,#c6b27a)"></span><span class="name">BBQ EGGPLANT</span><span class="price">100GF<span class="veg">V</span></span></div>

  <div class="row" style="left:222px;top:104px;width:150px"><span class="thumb ph" role="img" aria-label="Mixed vegetables" style="background:linear-gradient(135deg,#e7d26a,#7daa4a,#d9603c)"></span><span class="name">MIXED VEGGIE'S</span><span class="price">100GF<span class="veg">V</span></span><span class="desc">Stir-fried with garlic, chilli and oyster sauce</span></div>
  <div class="row" style="left:222px;top:132px;width:150px"><span class="thumb ph" role="img" aria-label="Mixed salad" style="background:linear-gradient(135deg,#e6efd6,#8ebd56)"></span><span class="name">MIX SALAD</span><span class="price">100GF<span class="veg">V</span></span><span class="desc">Fresh basil dressing</span></div>
  <div class="row" style="left:222px;top:160px;width:150px"><span class="thumb ph" role="img" aria-label="French fries" style="background:linear-gradient(135deg,#f2d68a,#d89a3a)"></span><span class="name">FRENCH FRIES</span><span class="price">100<span class="veg">V</span></span><span class="desc">House mayonnaise</span></div>
  <div class="row" style="left:222px;top:190px;width:150px"><span class="thumb ph" role="img" aria-label="Steamed rice" style="background:linear-gradient(135deg,#ffffff,#dedbd3)"></span><span class="name">STEAMED JASMIN RICE</span><span class="price">100<span class="veg">V</span></span></div>

  <div class="section-title" style="left:30px;top:234px">Dessert</div>
  <div class="card" style="left:20px;top:252px"><div class="photo ph" role="img" aria-label="Sorbet" style="position:relative;background:linear-gradient(135deg,#f2eee8,#e4a24a,#c24a3a)"><span class="badge">100GF</span></div><div class="name">SORBET</div><div class="desc">Fresh fruit, simple syrup and sorbet ice-cream</div></div>
  <div class="card" style="left:92px;top:252px"><div class="photo ph" role="img" aria-label="Creme brulee" style="position:relative;background:linear-gradient(135deg,#f4efe6,#e0a94a)"><span class="badge">100</span></div><div class="name">LINH'S SURPRISE CRÈME BRULÉE</div><div class="desc">Lemongrass</div></div>
  <div class="card" style="left:164px;top:252px"><div class="photo ph" role="img" aria-label="Chocolate cake" style="position:relative;background:linear-gradient(135deg,#f4f2ee,#5a3526,#e6e2dc)"><span class="badge">100</span></div><div class="name">VIETNAMESE CHOCOLATE CAKE</div><div class="desc">Coconut ice-cream</div></div>
  <div class="card" style="left:236px;top:252px"><div class="photo ph" role="img" aria-label="Pandan layer cake" style="position:relative;background:linear-gradient(135deg,#f2efe8,#8fc25a,#e8e3d8)"><span class="badge">100GF</span></div><div class="name">BANH DA LON</div><div class="desc">Asian gluten-free layer cake, slim fruit sorbet</div></div>
  <div class="card" style="left:308px;top:252px"><div class="photo ph" role="img" aria-label="Sweet lotus seed soup" style="position:relative;background:linear-gradient(135deg,#f6f3ec,#e6d6a8)"><span class="badge">100 GF</span></div><div class="name">CHÈVÀNAT SEN</div><div class="desc">Lotus seed sweet soup with lychee</div></div>

  <div class="ph" role="img" aria-label="Grilled meats with chili and star anise on a light table" style="left:0;top:340px;width:392px;height:186px;background:linear-gradient(180deg,rgba(255,255,255,0) 0%,#f0eaee 30%,#e7dce3 70%,#efe9ee 100%)"></div>
  <div class="ph" role="img" aria-label="Roasted meat and red chilies" style="left:40px;top:380px;width:312px;height:120px;border-radius:50%;background:radial-gradient(ellipse,rgba(168,52,40,.55) 0%,rgba(200,120,90,.35) 45%,rgba(231,220,227,0) 75%)"></div>

  <div class="footer-rule"></div>
  <div class="footer-band">www.lumvo.com</div>
</section>
<div class="page-label" style="left:494px;top:1170px">Page4</div>

</body>
</html>
```